Halvern Stationary Design

We're seeking a fresh and modern design for our stationery that captures the essence of our Real Estate brand. The current design, while functional, lacks visual appeal. We're looking for a more attractive and engaging design that showcases our professionalism and expertise in the real estate industry. I am attaching the current letter head and an image with a letter "P" as logo.

Target Market(s)

Real Estate Sales and Rentals

Industry/Entity Type

Real Estate

Requirements
Nice to have
• The owner seems to like the letter "P"

```html
<!DOCTYPE html>
<html lang="en">
<head>
<meta charset="utf-8">
<title>Halvern Stationery Design</title>
<link href="https://fonts.googleapis.com/css2?family=Lato:wght@400;700;900&display=swap" rel="stylesheet">
<style>
  :root {
    --navy: #262f66;
    --stage: #c4c4c6;
    --paper: #ffffff;
    --silver: #bcbcc2;
    --faint: #eeeef3;
    --accent: #f2c230;
    --icon: #3a9a5a;
    --label: #9c9c9c;
    --ink: #1c1c1c;
  }
  * { margin: 0; padding: 0; box-sizing: border-box; }
  html, body { width: 1200px; height: 593px; overflow: hidden; }
  body { position: relative; font-family: "Lato", sans-serif; background: var(--paper); }

  .stage { position: absolute; left: 0; top: 0; width: 764px; height: 593px; background: var(--stage); }

  .letterhead { position: absolute; top: 90px; width: 307px; height: 433px; background: var(--paper); overflow: hidden; }
  .letterhead--property { left: 58px; }
  .letterhead--rental { left: 398px; }

  .brand { position: absolute; left: 18px; top: 28px; width: 118px; text-align: center; color: var(--navy); font-weight: 900; }
  .brand__seal { width: 20px; height: 20px; border-radius: 50%; border: 1.5px solid var(--navy); background: var(--faint); margin: 0 auto 6px; }
  .brand__name { font-size: 10px; letter-spacing: 0.4px; line-height: 1; white-space: nowrap; }
  .brand__tag { font-size: 4.5px; letter-spacing: 4px; margin-top: 4px; }

  .contact { position: absolute; left: 186px; top: 29px; height: 47px; border-left: 1.2px solid var(--accent); padding-left: 12px; font-size: 5.2px; color: var(--ink); line-height: 1; }
  .contact__row { display: flex; align-items: flex-start; gap: 4px; margin-bottom: 2.6px; white-space: nowrap; }
  .contact__row:nth-child(2) { margin-top: 1.5px; }
  .contact__icon { width: 5px; height: 5px; flex: none; }
  .contact__name { color: var(--navy); font-weight: 700; }
  .contact__lines span { display: block; margin-bottom: 2.6px; }

  .watermark { position: absolute; left: 27px; top: 192px; width: 253px; text-align: center; color: var(--faint); font-weight: 900; font-size: 38px; letter-spacing: 2px; }

  .footer-wave { position: absolute; left: 0; top: 0; width: 307px; height: 433px; }
  .footer-line { position: absolute; left: 0; top: 420px; width: 307px; text-align: center; color: var(--paper); font-size: 5.4px; font-weight: 700; }

  .caption { position: absolute; top: 543px; width: 307px; text-align: center; font-size: 10px; font-weight: 700; letter-spacing: 1.6px; color: var(--ink); }
  .caption--property { left: 62px; }
  .caption--rental { left: 402px; }

  .logo-sheet { position: absolute; left: 764px; top: 0; width: 436px; height: 593px; }
  .logo { position: absolute; width: 180px; text-align: center; color: var(--navy); font-weight: 900; }
  .logo__seal { width: 34px; height: 34px; border-radius: 50%; border: 2px solid var(--navy); background: var(--faint); margin: 0 auto 8px; }
  .logo__name { font-size: 27px; letter-spacing: 1.5px; line-height: 1; }
  .logo__tag { font-size: 6.5px; letter-spacing: 3px; margin-top: 5px; }
  .logo--compact .logo__seal { width: 28px; height: 28px; margin-bottom: 6px; }
  .logo--compact .logo__name { font-size: 14px; letter-spacing: 0.6px; white-space: nowrap; }
  .logo--compact .logo__tag { letter-spacing: 5px; margin-top: 4px; }
  .logo--title .logo__name { font-size: 26px; letter-spacing: 0.5px; }
  .logo--title .logo__tag { text-align: left; padding-left: 6px; letter-spacing: 0.8px; margin-top: 4px; }

  .logo-divider { position: absolute; left: 66px; width: 324px; display: flex; align-items: center; gap: 6px; color: var(--label); font-size: 15px; font-weight: 700; letter-spacing: 2px; }
  .logo-divider::before, .logo-divider::after { content: ""; flex: 1; height: 1.5px; background: linear-gradient(90deg, rgba(156,156,156,0), var(--label)); }
  .logo-divider::after { background: linear-gradient(90deg, var(--label), rgba(156,156,156,0)); }
</style>
</head>
<body>

<div class="stage"></div>

<section class="letterhead letterhead--property">
  <div class="brand">
    <div class="brand__seal"></div>
    <div class="brand__name">HALVERN PROPERTY</div>
    <div class="brand__tag">SOLUTIONS</div>
  </div>
  <address class="contact" style="font-style:normal">
    <div class="contact__row">
      <svg class="contact__icon" viewBox="0 0 10 10"><path d="M5 0a3.5 3.5 0 0 0-3.5 3.5C1.5 6 5 10 5 10s3.5-4 3.5-6.5A3.5 3.5 0 0 0 5 0zm0 5a1.4 1.4 0 1 1 0-2.8A1.4 1.4 0 0 1 5 5z" fill="var(--icon)"/></svg>
      <div class="contact__lines"><span class="contact__name">Halvern Property Solutions</span><span>418 Larkmoor Avenue</span><span>Suite 6, Brindle, MA 02177</span></div>
    </div>
    <div class="contact__row">
      <svg class="contact__icon" viewBox="0 0 10 10"><path d="M2 0.5l2 2-1 1.3a6 6 0 0 0 3.2 3.2l1.3-1 2 2-1.3 1.5C4.5 9.5 0.5 5.5 0.5 1.8z" fill="var(--icon)"/></svg>
      <span>555-301-4826</span>
    </div>
    <div class="contact__row">
      <svg class="contact__icon" viewBox="0 0 10 10"><rect x="2.5" y="0.5" width="5" height="3" fill="none" stroke="var(--icon)"/><rect x="0.5" y="3.5" width="9" height="4" fill="var(--icon)"/><rect x="2.5" y="6.5" width="5" height="3" fill="#fff" stroke="var(--icon)"/></svg>
      <span>555-301-7190</span>
    </div>
    <div class="contact__row">
      <svg class="contact__icon" viewBox="0 0 10 10"><circle cx="5" cy="5" r="4.5" fill="var(--icon)"/><path d="M0.5 5h9M5 0.5c-2.5 3-2.5 6 0 9M5 0.5c2.5 3 2.5 6 0 9" stroke="#fff" stroke-width="0.7" fill="none"/></svg>
      <span>halvernsolutions.example</span>
    </div>
  </address>
  <div class="watermark">HALVERN</div>
  <svg class="footer-wave" viewBox="0 0 307 433" aria-hidden="true">
    <path d="M0 384 Q130 416 307 394 L307 397 Q130 420 0 390Z" fill="var(--silver)"/>
    <path d="M0 393 Q130 424 307 400 L307 433 L0 433Z" fill="var(--navy)"/>
  </svg>
  <p class="footer-line">Serving Boston's Real Estate Needs for 25+ Years!</p>
</section>

<section class="letterhead letterhead--rental">
  <div class="brand">
    <div class="brand__seal"></div>
    <div class="brand__name">HALVERN RENTAL</div>
    <div class="brand__tag">SOLUTIONS</div>
  </div>
  <address class="contact" style="font-style:normal">
    <div class="contact__row">
      <svg class="contact__icon" viewBox="0 0 10 10"><path d="M5 0a3.5 3.5 0 0 0-3.5 3.5C1.5 6 5 10 5 10s3.5-4 3.5-6.5A3.5 3.5 0 0 0 5 0zm0 5a1.4 1.4 0 1 1 0-2.8A1.4 1.4 0 0 1 5 5z" fill="var(--icon)"/></svg>
      <div class="contact__lines"><span class="contact__name">Halvern Rental Solutions</span><span>62 N.Ashcombe Avenue</span><span>#3 Wexley Green, MA 02181</span></div>
    </div>
    <div class="contact__row">
      <svg class="contact__icon" viewBox="0 0 10 10"><path d="M2 0.5l2 2-1 1.3a6 6 0 0 0 3.2 3.2l1.3-1 2 2-1.3 1.5C4.5 9.5 0.5 5.5 0.5 1.8z" fill="var(--icon)"/></svg>
      <span>555-301-4826</span>
    </div>
    <div class="contact__row">
      <svg class="contact__icon" viewBox="0 0 10 10"><rect x="2.5" y="0.5" width="5" height="3" fill="none" stroke="var(--icon)"/><rect x="0.5" y="3.5" width="9" height="4" fill="var(--icon)"/><rect x="2.5" y="6.5" width="5" height="3" fill="#fff" stroke="var(--icon)"/></svg>
      <span>555-301-7190</span>
    </div>
    <div class="contact__row">
      <svg class="contact__icon" viewBox="0 0 10 10"><circle cx="5" cy="5" r="4.5" fill="var(--icon)"/><path d="M0.5 5h9M5 0.5c-2.5 3-2.5 6 0 9M5 0.5c2.5 3 2.5 6 0 9" stroke="#fff" stroke-width="0.7" fill="none"/></svg>
      <span>halvernsolutions.example</span>
    </div>
  </address>
  <div class="watermark">HALVERN</div>
  <svg class="footer-wave" viewBox="0 0 307 433" aria-hidden="true">
    <path d="M0 384 Q130 416 307 394 L307 397 Q130 420 0 390Z" fill="var(--silver)"/>
    <path d="M0 393 Q130 424 307 400 L307 433 L0 433Z" fill="var(--navy)"/>
  </svg>
  <p class="footer-line">Serving Boston's Real Estate Needs for 25+ Years!</p>
</section>

<p class="caption caption--property">PROPERTY LETTER HEAD</p>
<p class="caption caption--rental">RENTAL LETTER HEAD</p>

<section class="logo-sheet">
  <div class="logo" style="left:37px;top:62px"><div class="logo__seal"></div><div class="logo__name">HALVERN</div><div class="logo__tag">PROPERTY SOLUTIONS</div></div>
  <div class="logo" style="left:232px;top:62px"><div class="logo__seal"></div><div class="logo__name">HALVERN</div><div class="logo__tag">RENTAL SOLUTIONS</div></div>
  <div class="logo-divider" style="top:161px">LOGO 1</div>

  <div class="logo" style="left:37px;top:201px"><div class="logo__seal"></div><div class="logo__name">HALVERN</div><div class="logo__tag">PROPERTY SOLUTIONS</div></div>
  <div class="logo" style="left:232px;top:201px"><div class="logo__seal"></div><div class="logo__name">HALVERN</div><div class="logo__tag">RENTAL SOLUTIONS</div></div>
  <div class="logo-divider" style="top:301px">LOGO 2</div>

  <div class="logo logo--compact" style="left:37px;top:338px"><div class="logo__seal"></div><div class="logo__name">HALVERN PROPERTY</div><div class="logo__tag">SOLUTIONS</div></div>
  <div class="logo logo--compact" style="left:232px;top:336px"><div class="logo__seal"></div><div class="logo__name">HALVERN RENTAL</div><div class="logo__tag">SOLUTIONS</div></div>
  <div class="logo-divider" style="top:421px">LOGO 3</div>

  <div class="logo logo--title" style="left:37px;top:466px"><div class="logo__seal"></div><div class="logo__name">Halvern</div><div class="logo__tag">PROPERTY SOLUTIONS</div></div>
  <div class="logo logo--title" style="left:232px;top:464px"><div class="logo__seal"></div><div class="logo__name">Halvern</div><div class="logo__tag">RENTAL SOLUTIONS</div></div>
  <div class="logo-divider" style="top:546px">LOGO 4</div>
</section>

</body>
</html>
```